Law Firm Website

We are looking to update our old, tired and very flat website. We have someone who will code and host the site but we need some design inspiration. The website will consist of no more than 2/3 pages, possibly with pop-ups for information. We already have all the blurb. We would like something distinctive, clean and eye-catching, using the purple and white theme that we already use on our firm stationery. Examples uploaded. Current website URL is www.dunmorewillett.example.

Industry/Entity Type

Law Firm

```html
<!DOCTYPE html>
<html lang="en">
<head>
<meta charset="utf-8">
<title>Dunmore &amp; Willett Solicitors</title>
<link rel="stylesheet" href="https://fonts.googleapis.com/css2?family=Bebas+Neue&family=Libre+Baskerville&family=Roboto:wght@300;400&family=Roboto+Slab:wght@300&family=Gochi+Hand&display=swap">
<style>
  :root {
    --purple: #5c4584;
    --purple-text: #4f3d7c;
    --band-grey: #dcdbe0;
    --panel-grey: #e6e5ea;
    --ink: #2b2b2b;
    --body: #3a3a3a;
    --muted: #9a9a9a;
    --white: #ffffff;
  }
  * { margin: 0; padding: 0; box-sizing: border-box; }
  html, body { width: 857px; height: 1200px; overflow: hidden; background: var(--white); }
  body { position: relative; font-family: "Roboto", sans-serif; font-weight: 300; color: var(--body); }

  .site-header { position: absolute; top: 0; left: 0; width: 857px; height: 200px; }
  .header-band { position: absolute; top: 98px; left: 0; width: 857px; height: 102px; background: var(--band-grey); }
  .brand { position: absolute; top: 50px; left: 0; width: 857px; text-align: center; }
  .brand-name { font-family: "Libre Baskerville", serif; font-size: 34px; color: var(--purple-text); line-height: 1; }
  .brand-sub { margin-top: 14px; font-family: "Libre Baskerville", serif; font-size: 12px; letter-spacing: 12px; color: #555; padding-left: 12px; }
  .nav-rule { position: absolute; top: 137px; left: 150px; width: 557px; height: 1px; background: var(--purple); }
  .main-nav { position: absolute; top: 149px; left: 0; width: 857px; display: flex; justify-content: center; gap: 26px; }
  .main-nav a { font-family: "Bebas Neue", sans-serif; font-size: 27px; color: #222; text-decoration: none; line-height: 1; white-space: nowrap; }

  .hero { position: absolute; top: 200px; left: 0; width: 857px; height: 417px; overflow: hidden; }
  .hero-photo { position: absolute; inset: 0; background: linear-gradient(100deg, #d9d8dc 0%, #c9c8cc 40%, #8f8e93 62%, #6e6d72 80%, #b7b8b2 100%); }
  .hero-title-band { position: absolute; top: 57px; left: 0; width: 857px; height: 146px; background: rgba(170,170,175,0.55); }
  .hero-title { position: absolute; top: 76px; left: 26px; font-family: "Roboto Slab", serif; font-weight: 300; font-size: 42px; line-height: 46px; color: var(--white); }
  .hero-tagline { position: absolute; top: 298px; left: 26px; font-family: "Roboto Slab", serif; font-weight: 300; font-size: 44px; line-height: 46px; color: var(--ink); }

  .about { position: absolute; top: 617px; left: 0; width: 857px; height: 236px; background: var(--panel-grey); }
  .about-photo-frame { position: absolute; top: 10px; left: 9px; width: 248px; height: 226px; background: #efeff1; }
  .about-photo { position: absolute; left: 17px; top: 0; width: 214px; height: 226px; background: linear-gradient(180deg, #7fb0e3 0%, #a9c9ea 35%, #bfae8c 60%, #8a7a62 100%); }
  .about-text { position: absolute; top: 24px; left: 285px; width: 540px; font-size: 14.6px; line-height: 19px; }
  .about-text p { margin-bottom: 18px; }
  .about-text .name { font-weight: 400; color: #222; }

  .expertise { position: absolute; top: 853px; left: 0; width: 857px; height: 171px; background: #ecebef; }
  .expertise-label { position: absolute; top: 0; left: 8px; width: 248px; height: 171px; background: var(--purple); color: var(--white); text-align: right; padding: 52px 20px 0 0; font-weight: 300; }
  .expertise-label small { display: block; font-size: 21px; line-height: 22px; }
  .expertise-label strong { display: block; font-weight: 300; font-size: 42px; line-height: 44px; }
  .practice-list { position: absolute; top: 8px; list-style: none; font-size: 14.8px; line-height: 20px; }

  .testimonials { position: absolute; top: 1024px; left: 0; width: 857px; height: 112px; background: var(--panel-grey); text-align: center; }
  .testimonials h2 { margin-top: 33px; font-weight: 300; font-size: 16.5px; color: #333; letter-spacing: 0.3px; }
  .testimonials blockquote { margin-top: 4px; font-family: "Gochi Hand", cursive; font-size: 18.5px; color: #222; }
  .quote-mark { position: absolute; font-family: "Roboto Slab", serif; font-size: 30px; color: #666; }

  .site-footer { position: absolute; top: 1136px; left: 0; width: 857px; height: 64px; }
  .partner-badge { position: absolute; top: 6px; left: 9px; width: 147px; height: 45px; background: #f3f3f3; border: 1px solid #e2e2e2; }
  .copyright { position: absolute; top: 7px; left: 0; width: 857px; text-align: center; font-size: 11.5px; color: var(--muted); }
  .legal-links { position: absolute; top: 7px; right: 3px; font-size: 11.5px; color: var(--muted); }
</style>
</head>
<body>
  <header class="site-header">
    <div class="header-band"></div>
    <div class="brand">
      <div class="brand-name">Dunmore &amp; Willett</div>
      <div class="brand-sub">SOLICITORS</div>
    </div>
    <div class="nav-rule"></div>
    <nav class="main-nav">
      <a href="#">Home</a>
      <a href="#">Area of Expertise</a>
      <a href="#">Daniel Dunmore</a>
      <a href="#">Peter Willett</a>
      <a href="#">Contact</a>
    </nav>
  </header>

  <section class="hero">
    <div class="hero-photo" role="img" aria-label="Photograph of a smiling man in a grey suit with arms outstretched in a city street"></div>
    <div class="hero-title-band"></div>
    <h1 class="hero-title">Dunmore &amp; Willett<br>Solicitors</h1>
    <p class="hero-tagline">for the service<br>you deserve</p>
  </section>

  <section class="about">
    <div class="about-photo-frame">
      <div class="about-photo" role="img" aria-label="Photograph of a gothic court building against a blue sky"></div>
    </div>
    <div class="about-text">
      <p>DUNMORE and WILLETT is a firm of solicitors with offices in Highfield, London and Ashcombe, Hertfordshire. This firm is authorised and regulated by the Legal Standards Authority, no.618305.</p>
      <p>VAT registered number: 731 4402 86</p>
      <p>Professional rules can be viewed on www.legalstandards.example/code-of-conduct.</p>
      <p>Know More about <span class="name">Daniel Dunmore</span> &amp; <span class="name">Peter Willett</span></p>
    </div>
  </section>

  <section class="expertise">
    <div class="expertise-label"><small>Areas of</small><strong>Expertise</strong></div>
    <ul class="practice-list" style="left:286px">
      <li>Company Matters</li><li>Commercial Matters</li><li>Commercial Crime</li><li>Litiagtion / Disputes</li>
      <li>Insolvency</li><li>Residential Conveyancing</li><li>Commercial Conveyancing</li><li>Wills &amp; Probate</li>
    </ul>
    <ul class="practice-list" style="left:569px">
      <li>Estate Planning</li><li>Powers of Attorney</li><li>Care of the Elderly</li><li>Court of Protection</li>
      <li>Divorce / Family</li><li>Pre-Nuptial Agreements</li><li>Intellectual Property</li><li>Media Law</li>
    </ul>
  </section>

  <section class="testimonials">
    <h2>CLIENT TESTIMONIALS</h2>
    <span class="quote-mark" style="left:36px;top:48px">&#8216;</span>
    <blockquote>thank you, thank you, thank you. your hard work and dedication has changed my life for better</blockquote>
    <span class="quote-mark" style="left:810px;top:38px">&#8217;</span>
  </section>

  <footer class="site-footer">
    <div class="partner-badge" role="img" aria-label="Family law association membership badge"></div>
    <div class="copyright">&copy; 2014. Dunmore &amp; Willett</div>
    <div class="legal-links">Legal Notice &nbsp;|&nbsp; Privacy Policy</div>
  </footer>
</body>
</html>
```